House Church design model for faith-based organization

A design is needed for a house church model (Christian, faith-based). I’m looking for a graphic to convey four house church hallmarks showing the balance of member engagement. The four-part model includes - God’s Presence, Community, Discipleship, Outreach. The model should consist of the text for the four parts and the words - House Church

Perhaps a circular/modular design with House Church in the center. Using equally-sized interlocking slices or winged parts (graphically speaking, but not angelic wings) may help convey a balanced approach. It isn’t a process and should not appear in progressive steps, but the order (as listed) is used when explaining the concept. The model will be used for members to evaluate monthly focus.

I’m open to interpretation of the design and artwork. Designers should not feel a need to utilize cliché-like Christian symbols. However, if done minimally (and perhaps first century-like), they could be of interest (but are not required). Keeping it abstract may help readability and convey a roots/back-to-basics feel.

The artwork will be used for a video and PowerPoint presentation. It should be vector-based for simple movement/animation.

Additional thoughts:
Readable, not complex
Interesting interlocking design found at: https://www.pixelvarno.com/ring-module-infographic-choices-segments-stages-layout-loop-diagram-chart-round-graph-image507318264

Target Market(s)

To existing members (for reflection) and for those seeking a simpler church experience.

Requirements
Must have
• Simple, readable design, ability to reproduce for PowerPoint, video, and web. Prefer simple illustrations rather than images.
Nice to have
• The design should create a calming sense of focus on four priorities vs. the complexity of structure/requirements often found in the church experience.
Should not have
• Not crazy about puzzle pieces. Please avoid using all CAPS and serif fonts. Should not use complex images or photos.

```html
<!DOCTYPE html>
<html lang="en">
<head>
<meta charset="utf-8">
<title>House Church Model</title>
<link rel="stylesheet" href="https://fonts.googleapis.com/css2?family=Open+Sans:wdth,wght@75..100,600..700&display=swap">
<style>
  :root {
    --bg: #ffffff;
    --presence: #f0b820;
    --community: #7abd26;
    --discipleship: #af70de;
    --outreach: #f25c42;
    --label: #111111;
    --center-label: #333333;
    --spoke: #e4e4e4;
  }
  html, body {
    margin: 0;
    padding: 0;
    overflow: hidden;
    background: var(--bg);
  }
  .canvas {
    width: 1200px;
    height: 1000px;
    position: relative;
    background: var(--bg);
  }
  .model {
    position: absolute;
    inset: 0;
    width: 1200px;
    height: 1000px;
  }
  .ring {
    fill: none;
    stroke-width: 46;
  }
  .ring--presence { stroke: var(--presence); }
  .ring--community { stroke: var(--community); }
  .ring--discipleship { stroke: var(--discipleship); }
  .ring--outreach { stroke: var(--outreach); }
  .spoke {
    stroke: var(--spoke);
    stroke-width: 6;
    stroke-linecap: round;
  }
  .hallmark {
    font-family: "Open Sans", sans-serif;
    font-stretch: 75%;
    font-weight: 700;
    font-size: 27px;
    fill: var(--label);
    text-anchor: middle;
  }
  .center-title {
    font-family: "Open Sans", sans-serif;
    font-stretch: 75%;
    font-weight: 700;
    font-size: 37px;
    fill: var(--center-label);
    text-anchor: middle;
  }
</style>
</head>
<body>
<main class="canvas">
  <svg class="model" viewBox="0 0 1200 1000" xmlns="http://www.w3.org/2000/svg" role="img" aria-label="House Church model: God's Presence, Community, Discipleship, Outreach">
    <g class="spokes">
      <line class="spoke" x1="600" y1="440" x2="600" y2="400"/>
      <line class="spoke" x1="600" y1="560" x2="600" y2="600"/>
      <line class="spoke" x1="655" y1="500" x2="700" y2="500"/>
      <line class="spoke" x1="545" y1="500" x2="499" y2="500"/>
    </g>
    <g class="rings">
      <circle class="ring ring--presence" cx="600" cy="318" r="97"/>
      <circle class="ring ring--community" cx="783" cy="500" r="97"/>
      <circle class="ring ring--discipleship" cx="600" cy="682" r="97"/>
      <circle class="ring ring--outreach" cx="416" cy="500" r="97"/>
    </g>
    <g class="labels">
      <text class="hallmark" x="600" y="314">God’s</text>
      <text class="hallmark" x="600" y="342">Presence</text>
      <text class="hallmark" x="783" y="507">Community</text>
      <text class="hallmark" x="600" y="689">Discipleship</text>
      <text class="hallmark" x="416" y="510">Outreach</text>
      <text class="center-title" x="600" y="495">House</text>
      <text class="center-title" x="600" y="530">Church</text>
    </g>
  </svg>
</main>
</body>
</html>
```